Webdesign for Tenora Homes Business

We need a professional and slim design for a hight quality Tenora Homes website which is not overcrowded with too much information and has a clear and easily structure to read. The visitor should get an instant impression what he can do at a glance.

The goal of this contest is to get a design for building a prototype of the website and to attract our client and owner of the site by a good looking prototype and not just a wireframe. Therefore we don't need an HTML-coded design at this early project-stage. We only expect getting a simple bitmap or vector-graphic design.

Actually we don't have a logo. Use a placeholder or feel free to design a simple one by yourself.

Last but not least if you have a good idea just include it in to your design.

Our goal is to get a design for building a prototype of the website and to attract our client by a good looking prototype and not just a wireframe.

Target Market(s)

People who want to spend money to rent a good quality property. Not only the riches. These could be business people and also demanding families as well.

Industry/Entity Type

Building

Colors
85cae6

Requirements
Must have
• We need two sites, a start site and a property-details site. Each site has to include the following points:

1.) start site
- search mask (location, date to choose, quanity of guests)
- show some properties (highlights, special offers etc.)
- show login/register link

2.) property site
- Location in Vorlen Map
- Photos, Description, Amenities, Calendar (available,not available), Contact, Reviews

These are some sites which I like from a design prospective
- http://www.stayquelo.com
- http://www.lodvanta.com/
- http://www.dwellirox.com/
- http://www.plomavi.com

These are some sites which I dislike:
1.) http://www.gallic-estatio.com/guides/france/rent/
2.) http://www.solohomvenu.co.za/property-rentals.htm

We don't need an HTML-coded design at this early project-stage. We only expect getting a simple bitmap or vector-graphic design. Maybe with the PSD-file (or wathever program you use) that we can pick-out some elements for building the prototype.

```html
<!DOCTYPE html>
<html lang="en">
<head>
<meta charset="utf-8">
<title>Tenora Homes — Find Your Perfect Fit</title>
<link rel="stylesheet" href="https://fonts.googleapis.com/css2?family=Oswald:wght@400;500&family=Roboto:wght@400;500&display=swap">
<style>
  :root {
    --brand: #85cae6;
    --brand-text: #6cbde2;
    --accent: #f06a12;
    --ink: #333333;
    --ink-soft: #555555;
    --line: #e2e2e2;
    --card-border: #e6e6e6;
    --card-bg: #fafafa;
    --white: #ffffff;
    --panel: rgba(48, 52, 58, 0.78);
    --footer-top: #e4e4e4;
    --footer-bottom: #ffffff;
  }
  * { box-sizing: border-box; margin: 0; padding: 0; }
  html, body { width: 952px; height: 1200px; overflow: hidden; }
  body { position: relative; background: var(--white); font-family: "Roboto", Arial, sans-serif; color: var(--ink); }
  .abs { position: absolute; }

  /* header */
  .site-header { position: absolute; left: 0; top: 0; width: 952px; height: 103px; background: var(--white); }
  .brand-name { left: 58px; top: 64px; font-family: "Roboto", sans-serif; font-weight: 500; font-size: 21px; color: #3d3d3d; letter-spacing: 0.3px; }
  .main-nav { left: 272px; top: 78px; display: flex; gap: 16px; font-size: 10.5px; letter-spacing: 0.4px; color: #3a3a3a; }
  .account-links { right: 59px; top: 73px; font-family: "Oswald", sans-serif; font-size: 13px; color: #333; }
  .account-links .login { color: var(--brand-text); }
  .account-links .sep { margin: 0 6px; }

  /* hero */
  .hero { left: 0; top: 103px; width: 952px; height: 407px; }
  .hero-photo { width: 100%; height: 100%;
    background: linear-gradient(100deg, #8fb6e0 0%, #b9d2ea 30%, #e9e4dc 52%, #d98a45 72%, #e7e3dd 86%, #cf7c3c 100%); }
  .search-panel { left: 219px; top: 125px; width: 514px; height: 159px; background: var(--panel); border-radius: 4px; }
  .search-title { position: absolute; left: 0; right: 0; top: 2px; text-align: center; font-family: "Oswald", sans-serif; font-weight: 500; font-size: 44px; color: var(--white); }
  .search-input { left: 14px; top: 67px; width: 443px; height: 38px; background: var(--white); border-radius: 3px 0 0 3px; font-size: 15px; color: #8a8a8a; padding: 10px 14px; }
  .search-btn { left: 457px; top: 67px; width: 43px; height: 38px; background: var(--accent); border-radius: 0 3px 3px 0; }
  .search-btn svg { display: block; margin: 8px auto 0; }
  .select { top: 121px; height: 26px; background: var(--white); border-radius: 2px; font-size: 10.5px; color: #777; padding: 7px 9px; }
  .select .caret { position: absolute; right: 8px; top: 11px; width: 0; height: 0; border-left: 5px solid transparent; border-right: 5px solid transparent; border-top: 5px solid #888; }
  .calendar-icon { left: 261px; top: 124px; }

  /* intro */
  .section-title { font-family: "Oswald", sans-serif; font-size: 21px; color: var(--brand-text); font-weight: 400; }
  .intro-title { left: 58px; top: 531px; }
  .intro-text { left: 58px; top: 572px; width: 602px; font-size: 9.8px; line-height: 17px; color: var(--ink-soft); }
  .intro-text p + p { margin-top: 4px; }
  .devices { left: 680px; top: 560px; width: 208px; height: 102px; background: linear-gradient(135deg, #2c2c2c, #c9dbe8 45%, #d8e7cc 70%, #2c2c2c); border-radius: 4px; }
  .divider { left: 58px; top: 700px; width: 835px; height: 1px; background: var(--line); }

  /* featured */
  .featured-title { left: 58px; top: 717px; }
  .card { top: 764px; width: 193px; height: 242px; background: var(--card-bg); border: 1px solid var(--card-border); }
  .card-photo { position: absolute; left: 12px; top: 11px; width: 169px; height: 118px; }
  .card-body { position: absolute; left: 12px; top: 140px; width: 172px; font-size: 10.5px; line-height: 14.5px; color: var(--ink-soft); }
  .card-body b { color: var(--ink); font-weight: 500; font-size: 11px; }
  .card-body .desc { margin-top: 4px; }
  .card-foot { position: absolute; left: 12px; right: 10px; top: 208px; height: 22px; display: flex; justify-content: space-between; align-items: center; }
  .price { font-family: "Oswald", sans-serif; font-size: 16px; color: var(--brand-text); }
  .more { font-size: 9.5px; color: var(--ink); }
  .card.special { left: 703px; top: 725px; width: 191px; height: 281px; background: var(--brand); border: 1px solid #d6e9f2; }
  .card.special .card-photo { left: 0; top: 0; width: 189px; height: 167px; }
  .card.special .card-body { left: 10px; top: 175px; color: #2f4b58; }
  .card.special .card-body b { color: #1f3440; }
  .card.special .card-foot { left: 10px; top: 244px; }
  .card.special .price { color: var(--white); }
  .ribbon { position: absolute; left: 0; top: 0; }

  /* footer */
  .site-footer { left: 0; top: 1025px; width: 952px; height: 175px; background: linear-gradient(var(--footer-top), var(--footer-bottom) 60%); }
  .footer-col { top: 22px; font-size: 10px; color: var(--ink-soft); }
  .footer-col h4 { font-weight: 400; font-size: 12px; color: var(--ink); margin-bottom: 6px; }
  .footer-col li { list-style: none; line-height: 21px; }
  .social { left: 634px; top: 60px; display: flex; gap: 6.5px; }
  .social span { width: 26px; height: 26px; border-radius: 50%; border: 2px solid #d9d9d9; }
  .footer-brand { left: 620px; top: 90px; width: 112px; height: 60px; background: var(--white); }
  .footer-brand span { position: absolute; left: 0; right: 0; top: 38px; text-align: center; font-family: "Roboto", sans-serif; font-weight: 500; font-size: 12px; color: #3d3d3d; }
  .copyright { left: 743px; top: 132px; font-size: 9px; color: #777; }
</style>
</head>
<body>

<header class="site-header">
  <div class="abs brand-name">TENORA HOMES</div>
  <nav class="abs main-nav">
    <span>SEARCH</span><span>REVIEWS</span><span>RENTER RESOURCES</span><span>ADVERTISE</span>
  </nav>
  <div class="abs account-links"><span class="login">Log In</span><span class="sep">|</span><span>Register</span></div>
</header>

<section class="abs hero">
  <div class="hero-photo" role="img" aria-label="Modern apartment buildings with orange panels and balconies under a blue sky"></div>
  <div class="abs search-panel">
    <h1 class="search-title">Find Your Perfect Fit</h1>
    <div class="abs search-input">Enter City, Zip or State</div>
    <div class="abs search-btn">
      <svg width="24" height="22" viewBox="0 0 24 22"><circle cx="9" cy="9" r="6.5" fill="none" stroke="#fff" stroke-width="2.6"/><line x1="13.5" y1="13.5" x2="21" y2="20" stroke="#fff" stroke-width="3.4" stroke-linecap="round"/></svg>
    </div>
    <div class="abs select" style="left:15px;width:114px">Location<i class="caret"></i></div>
    <div class="abs select" style="left:143px;width:114px">Choose Date</div>
    <svg class="abs calendar-icon" width="22" height="20" viewBox="0 0 22 20">
      <rect x="0.5" y="0.5" width="21" height="19" fill="#fff" stroke="#7aa1cc"/>
      <rect x="0.5" y="0.5" width="21" height="4" fill="#7aa1cc"/>
      <g stroke="#b5cbe2" stroke-width="1"><line x1="0" y1="9.5" x2="22" y2="9.5"/><line x1="0" y1="14.5" x2="22" y2="14.5"/><line x1="5.5" y1="4" x2="5.5" y2="20"/><line x1="11" y1="4" x2="11" y2="20"/><line x1="16.5" y1="4" x2="16.5" y2="20"/></g>
    </svg>
    <div class="abs select" style="left:293px;width:114px">No of Guest<i class="caret"></i></div>
  </div>
</section>

<section>
  <h2 class="abs section-title intro-title">Find Renting Property Anywhere</h2>
  <div class="abs intro-text">
    <p>Aliquam molestie, mi et imperdiet euismod, dui purus auctor tellus, et interdum lacus lectus et ante. Sed accumsan sollicitudin sapien, sit amet adipiscing turpis gravida ac. In congue, neque ac lobortis volutpat, libero mauris varius mi, vitae suscipit ipsum ligula vitae risus. Duis aliquam nibh a dui iaculis viverra id a velit. Vivamus egestas risus in magna varius commodo. Sed semper viverra egestas. Etiam pretium porttitor lectus, vel ornare neque porta volutpat.</p>
    <p>Ut et scelerisque ante. Donec erat purus, faucibus vitae congue vel, porttitor nec lectus. Aenean a nibh eget turpis vehicula tempus ac sed massa. Vestibulum dolor nulla, ultrices ac tincidunt sed, laoreet non est.</p>
  </div>
  <div class="abs devices" role="img" aria-label="Laptop, tablet and phone showing the property search map"></div>
  <div class="abs divider"></div>
</section>

<section>
  <h2 class="abs section-title featured-title">Featured Property</h2>

  <article class="abs card" style="left:58px">
    <div class="card-photo" role="img" aria-label="Modern white villa with terrace" style="background:linear-gradient(#6f9fd8,#e8e2d6 55%,#8a7a62)"></div>
    <div class="card-body"><b>Location:</b> Guttenberg, NJ<div class="desc"><b>Description:</b> Nemo enim ipsam voluptatem voluptas sit aspernatur aut oditaut...</div></div>
    <div class="card-foot"><span class="price">$625,000</span><span class="more">More Details &gt;&gt;</span></div>
  </article>

  <article class="abs card" style="left:272px">
    <div class="card-photo" role="img" aria-label="Stone family house at dusk" style="background:linear-gradient(#1c3f7a,#6a6256 55%,#3f5a2c)"></div>
    <div class="card-body"><b>Location:</b> Guttenberg, NJ<div class="desc"><b>Description:</b> Nemo enim ipsam voluptatem voluptas sit aspernatur aut oditaut...</div></div>
    <div class="card-foot"><span class="price">$625,000</span><span class="more">More Details &gt;&gt;</span></div>
  </article>

  <article class="abs card" style="left:486px">
    <div class="card-photo" role="img" aria-label="Large white mansion with driveway" style="background:linear-gradient(#7fa7d6,#e9e6e0 55%,#8f8a80)"></div>
    <div class="card-body"><b>Location:</b> Guttenberg, NJ<div class="desc"><b>Description:</b> Nemo enim ipsam voluptatem voluptas sit aspernatur aut oditaut...</div></div>
    <div class="card-foot"><span class="price">$625,000</span><span class="more">More Details &gt;&gt;</span></div>
  </article>

  <article class="abs card special">
    <div class="card-photo" role="img" aria-label="Brick family house with front lawn" style="background:linear-gradient(#9ec4e8,#a8735a 50%,#5f8a3e)"></div>
    <svg class="ribbon" width="112" height="112" viewBox="0 0 112 112">
      <polygon points="0,0 112,0 0,112" fill="#f06a12"/>
      <g transform="translate(34,40) rotate(-45)" font-family="Oswald, sans-serif" font-size="15" fill="#fff" text-anchor="middle">
        <text x="0" y="0">SPECIAL</text>
        <text x="0" y="16">OFFERS</text>
      </g>
    </svg>
    <div class="card-body"><b>Location:</b> Guttenberg, NJ<div class="desc"><b>Description:</b> Nemo enim ipsam voluptatem voluptas sit aspernatur aut oditaut...</div></div>
    <div class="card-foot"><span class="price">$625,000</span><span class="more">More Details &gt;&gt;</span></div>
  </article>
</section>

<footer class="abs site-footer">
  <div class="abs footer-col" style="left:59px"><h4>Footer Navigation</h4><ul><li>Sus in magna varius</li><li>Commodo</li><li>Sed semper viverra</li><li>Egestas</li><li>Etiam pretium</li></ul></div>
  <div class="abs footer-col" style="left:241px"><h4>Footer Navigation</h4><ul><li>Sus in magna varius</li><li>Commodo</li><li>Sed semper viverra</li><li>Egestas</li><li>Etiam pretium</li></ul></div>
  <div class="abs footer-col" style="left:424px"><h4>Footer Navigation</h4><ul><li>Sus in magna varius</li><li>Commodo</li><li>Sed semper viverra</li><li>Egestas</li><li>Etiam pretium</li></ul></div>
  <div class="abs footer-col" style="left:631px"><h4>Join Us</h4></div>
  <div class="abs social">
    <span style="background:#3b5a9a"></span><span style="background:#29a9e1"></span><span style="background:#1f7bb6"></span><span style="background:#d34836"></span><span style="background:#c8232c"></span><span style="background:#e8e8e8"></span><span style="background:#c4302b"></span>
  </div>
  <div class="abs footer-brand"><span>TENORA HOMES</span></div>
  <div class="abs copyright">Copyright © 2014. All Right Reserved</div>
</footer>

</body>
</html>
```